RVT studios

rvt studios is an interior design firm in omaha, NE. Offering complete residential/commercial design. Exterior, int finishes, cabinets, furniture, window covering. Have been in business for 25 yrs. Lived in and/or completed work in LA, NYC, PHX, MIami, London, Canada, Mexico. We would like to see a marketing flyer with clean, architectural design. Modern .Flyer will be on display at open houses & mailed to perspective clients. Dont want a lot of color. Prefer whites/black, greys or brown. Maybe small accent of blue like logo. Block architectural lettering. do not need to use all photos. but use at least one from each of the three projects. thanks for you time

please change/add on any and all submissions the following add: Dana Whitcombe, Principal (in info section not on logo) change: Info@rvtstudios.com, not dana @rvtstudios.com add: back design, would like to use as many photos as possible thanks you

```html
<!DOCTYPE html>
<html lang="en">
<head>
<meta charset="utf-8">
<title>RVT studios – Flyer</title>
<link rel="stylesheet" href="https://fonts.googleapis.com/css2?family=Libre+Baskerville:wght@400;700&display=swap">
<style>
  :root {
    --canvas-bg: #e6e6e6;
    --paper: #ffffff;
    --brown: #4b3527;
    --brown-text: #46301f;
    --body-text: #3a3a3a;
    --accent-blue: #1f6db5;
    --ring-grey: #dcdcdc;
    --white: #ffffff;
  }
  * { box-sizing: border-box; margin: 0; padding: 0; }
  html, body {
    width: 1200px; height: 1000px; overflow: hidden;
    background: var(--canvas-bg);
  }
  .flyer {
    position: absolute; left: 90px; top: 163px;
    width: 1020px; height: 672px;
    background: var(--paper);
    box-shadow: 0 4px 14px rgba(0,0,0,.18);
    overflow: hidden;
    font-family: "Libre Baskerville", Georgia, serif;
  }
  .flyer-art { position: absolute; inset: 0; width: 1020px; height: 672px; }
  .brand {
    position: absolute; left: 60px; top: 52px;
    color: var(--brown-text); font-weight: 700; line-height: 1;
  }
  .brand-main { display: block; font-size: 92px; letter-spacing: -1px; }
  .brand-sub { display: block; font-size: 46px; margin-top: 8px; }
  .intro {
    position: absolute; left: 60px; top: 225px; width: 330px;
    color: var(--body-text); font-size: 15.5px; line-height: 20.5px;
  }
  .intro p + p { margin-top: 7px; }
  .callout {
    position: absolute; left: 605px; top: 262px; width: 160px;
    text-align: center; color: var(--white);
    font-weight: 700; font-size: 20px; line-height: 27px;
  }
  .footer-brand {
    position: absolute; left: 62px; top: 545px; width: 106px;
    text-align: center; color: var(--white); font-weight: 400; line-height: 1;
  }
  .footer-brand-main { display: block; font-size: 27px; }
  .footer-brand-sub { display: block; font-size: 24px; margin-top: 4px; }
  .footer-brand-tag { display: block; font-size: 11px; margin-top: 8px; }
  .footer-divider {
    position: absolute; left: 176px; top: 547px;
    width: 3px; height: 88px; background: var(--accent-blue);
  }
  .contact {
    position: absolute; left: 195px; top: 548px;
    color: var(--white); font-weight: 700; list-style: none;
  }
  .contact-phone { font-size: 29px; line-height: 36px; }
  .contact-line { font-size: 18px; line-height: 27px; }
</style>
</head>
<body>
<main class="flyer">
  <svg class="flyer-art" viewBox="0 0 1020 672" aria-hidden="false">
    <defs>
      <radialGradient id="tone-wine" cx="45%" cy="45%" r="60%">
        <stop offset="0" stop-color="#8a6a55"/><stop offset="1" stop-color="#3a2418"/>
      </radialGradient>
      <radialGradient id="tone-library" cx="50%" cy="45%" r="60%">
        <stop offset="0" stop-color="#f4efe6"/><stop offset="1" stop-color="#c9b79a"/>
      </radialGradient>
      <radialGradient id="tone-kitchen" cx="50%" cy="40%" r="60%">
        <stop offset="0" stop-color="#efe6d4"/><stop offset="1" stop-color="#9b8a72"/>
      </radialGradient>
      <radialGradient id="tone-living" cx="50%" cy="50%" r="60%">
        <stop offset="0" stop-color="#8c8580"/><stop offset="1" stop-color="#2d2622"/>
      </radialGradient>
    </defs>

    <g class="wave">
      <path d="M0,452 C130,535 330,540 520,468 C700,400 860,330 1020,318 L1020,672 L0,672 Z" fill="var(--ring-grey)"/>
      <path d="M0,462 C130,545 330,548 520,476 C700,408 860,340 1020,328 L1020,672 L0,672 Z" fill="var(--brown)"/>
    </g>

    <g class="photo-ring">
      <circle cx="527" cy="232" r="156" fill="var(--ring-grey)"/>
      <circle cx="527" cy="232" r="148" fill="var(--white)"/>
      <g role="img" aria-label="Photo: stone-walled wine cellar with arched wine display">
        <circle cx="527" cy="232" r="128" fill="url(#tone-wine)"/>
      </g>
    </g>
    <g class="photo-ring">
      <circle cx="787" cy="194" r="160" fill="var(--ring-grey)"/>
      <circle cx="787" cy="194" r="152" fill="var(--white)"/>
      <g role="img" aria-label="Photo: white built-in library shelving with french doors">
        <circle cx="787" cy="194" r="138" fill="url(#tone-library)"/>
      </g>
    </g>
    <g class="photo-ring">
      <circle cx="595" cy="432" r="136" fill="var(--ring-grey)"/>
      <circle cx="595" cy="432" r="128" fill="var(--white)"/>
      <g role="img" aria-label="Photo: cream kitchen cabinets with gas range">
        <circle cx="595" cy="432" r="110" fill="url(#tone-kitchen)"/>
      </g>
    </g>
    <g class="photo-ring">
      <circle cx="812" cy="448" r="162" fill="var(--ring-grey)"/>
      <circle cx="812" cy="448" r="154" fill="var(--white)"/>
      <g role="img" aria-label="Photo: open living area with vaulted beamed ceiling and kitchen island">
        <circle cx="812" cy="448" r="134" fill="url(#tone-living)"/>
      </g>
    </g>
    <g class="callout-badge">
      <circle cx="685" cy="329" r="112" fill="var(--white)"/>
      <circle cx="685" cy="329" r="104" fill="var(--accent-blue)"/>
    </g>
  </svg>

  <h1 class="brand">
    <span class="brand-main">RVT</span>
    <span class="brand-sub">Studios</span>
  </h1>

  <section class="intro">
    <p>Rvt studios has offered complete design services for residential and commercial projects for over 25 years. Our diversity has allowed RVT studios to design new construction and renovation projects in New York, California, Florida, Arizona and Mexico.</p>
    <p>We can work with your builder to coordinate the many architectural details required to create your personal space. Thus allowing your project to progress smoothly and more cost effectively.</p>
  </section>

  <p class="callout">Please call to talk about your upcoming project</p>

  <div class="footer-brand">
    <span class="footer-brand-main">RVT</span>
    <span class="footer-brand-sub">Studios</span>
    <span class="footer-brand-tag">Complete Design</span>
  </div>
  <div class="footer-divider"></div>
  <ul class="contact">
    <li class="contact-phone">402-555-0148</li>
    <li class="contact-line">dana@rvtstudios.com</li>
    <li class="contact-line">www.rvtstudios.com</li>
  </ul>
</main>
</body>
</html>
```